Zelvora - Creative Robotics

We are a software house for Audio Visual Systems integration/automation and home automation. we develop innovative software to automate a variety of devices mainly related to audio visuals and we design touch panel user interfaces to control these systems.

We would like to see designs that stick to our colours and theme, which you can find on our webpage www.zelvora-sample.com.au

The final design should communicate touch panels, innovation, software and automation.

Industry/Entity Type

Software

Requirements
Must have
• The business card must show the following information:
Name example : Derek Halvey
Qualification example: B Eng ICT(CompSys) Dip EngPrac
Title example : Control Systems Programmer
Mobile Phone, Company phone, Email address ,Company website

```html
<!DOCTYPE html>
<html lang="en">
<head>
<meta charset="utf-8">
<title>Zelvora - Creative Robotics business card</title>
<link href="https://fonts.googleapis.com/css2?family=Source+Sans+3:wght@400;600;700&display=swap" rel="stylesheet">
<style>
  :root {
    --page-bg: #ffffff;
    --card-bg: #2f2f2f;
    --text-light: #ffffff;
    --brand-green: #1fa463;
    --brand-blue: #1b75c4;
    --label-ink: #2f2f2f;
  }
  html, body {
    margin: 0;
    padding: 0;
    overflow: hidden;
    background: var(--page-bg);
  }
  .canvas {
    position: relative;
    width: 1200px;
    height: 900px;
    background: var(--page-bg);
    font-family: "Source Sans 3", "Myriad Pro", sans-serif;
    overflow: hidden;
  }
  .card {
    position: absolute;
    top: 129px;
    width: 395px;
    height: 647px;
    border-radius: 22px;
    background: var(--card-bg);
    color: var(--text-light);
    overflow: hidden;
  }
  .card--front { left: 149px; }
  .card--back { left: 655px; }

  .brand {
    position: absolute;
    left: 0;
    right: 0;
    top: 250px;
    text-align: center;
  }
  .brand__mark {
    display: block;
    width: 84px;
    height: 70px;
    margin: 0 auto 16px;
    background: var(--brand-blue);
  }
  .brand__name {
    display: block;
    font-size: 52px;
    font-weight: 600;
    line-height: 1;
    letter-spacing: 0.5px;
    color: var(--brand-green);
  }
  .brand__tagline {
    display: block;
    margin-top: 4px;
    font-size: 11px;
    font-weight: 700;
    color: var(--text-light);
  }

  .contact {
    position: absolute;
    left: 40px;
    top: 405px;
  }
  .contact__name {
    margin: 0;
    font-size: 20px;
    font-weight: 400;
    line-height: 26px;
  }
  .contact__title {
    margin: 0 0 24px;
    font-size: 18px;
    font-weight: 400;
    line-height: 26px;
  }
  .contact__list {
    list-style: none;
    margin: 0;
    padding: 0;
  }
  .contact__item {
    display: flex;
    align-items: center;
    height: 25.3px;
    font-size: 19px;
    line-height: 1;
  }
  .contact__label {
    display: inline-flex;
    align-items: center;
    justify-content: center;
    width: 16px;
    height: 16px;
    margin-right: 11px;
    background: var(--text-light);
    color: var(--label-ink);
    font-size: 13px;
    font-weight: 700;
  }
</style>
</head>
<body>
  <main class="canvas">
    <section class="card card--front" aria-label="Card front">
      <div class="brand">
        <span class="brand__mark" aria-hidden="true"></span>
        <span class="brand__name">Zelvora</span>
        <span class="brand__tagline">Creative Robotics</span>
      </div>
    </section>

    <section class="card card--back" aria-label="Card back">
      <div class="contact">
        <h1 class="contact__name">Derek Halvey</h1>
        <p class="contact__title">Control Systems Programmer</p>
        <ul class="contact__list">
          <li class="contact__item"><span class="contact__label">Q</span>B Eng ICT(CompSys), Dip EngPrac</li>
          <li class="contact__item"><span class="contact__label">P</span>0249 555 018</li>
          <li class="contact__item"><span class="contact__label">M</span>0400 555 742</li>
          <li class="contact__item"><span class="contact__label">W</span>www.zelvora-sample.com.au</li>
          <li class="contact__item"><span class="contact__label">E</span>support@zelvora-sample.com.au</li>
        </ul>
      </div>
    </section>
  </main>
</body>
</html>
```